Financial Services Company Needs New UI/UX

Hello!

We would like to see some UI/UX ideas for our software platform. I've attached a screen capture of our current "dashboard" (or main home page, essentially). We're looking for a very simple, clean, sleek design as there are many different pages throughout the system that will all need to coordinate. You can also view our website to see the colors and general "look" we have on there. It would be ideal for the portal to coordinate with the website since that is how they access the login page. Please submit your best ideas for the dashboard and we will reach out to our favorite designer to move forward with the rest of the pages. You can find our color hex codes on our website on the "Media" page. Should you need any other supporting logos or files please send us a message and we will try to accommodate.

Thanks!

Website: www.tradevanecredit.example

Target Market(s)

Our clients are contractors in the construction industry and our software helps them manage material purchases for their jobs.

Industry/Entity Type

Financial Service

Font styles to use
Sans Serif

Requirements
Must have
• The same content and language as the current dashboard but an updated look.
Should not have
• Too much distraction or busy patterns, we're looking for clean and simple and user friendly. Likely a solid or subtly textured background would be best.

```html
<!DOCTYPE html>
<html lang="en">
<head>
<meta charset="utf-8">
<title>Tradevane Credit Dashboard</title>
<link href="https://fonts.googleapis.com/css2?family=Roboto:wght@300;400;500;700&display=swap" rel="stylesheet">
<style>
:root{
  --mat:#6b727c;
  --header:#24282b;
  --sidebar:#2b2f33;
  --sidebar-active:#1e2124;
  --nav-text:#c9ced3;
  --header-text:#8e959c;
  --blue:#3f87c9;
  --orange:#e2561b;
  --green:#3aae4a;
  --brown:#a87a44;
  --band:#eef1f4;
  --card:#ffffff;
  --ink:#222;
  --muted:#333;
  --panel-head:#d4dee6;
  --line:#e6e9ec;
  --col-head:#b8703a;
}
*{box-sizing:border-box;margin:0;padding:0}
html,body{width:1200px;height:743px;overflow:hidden}
body{background:var(--mat);font-family:'Roboto',sans-serif;position:relative}
.app{position:absolute;left:68px;top:72px;width:1064px;height:600px;background:#fff;overflow:hidden}
.topbar{position:absolute;left:0;top:0;width:1064px;height:67px;background:var(--header)}
.brand{position:absolute;left:0;top:0;width:194px;height:67px;display:flex;align-items:center;padding-left:26px;color:#fff;font-size:13px;font-weight:400;gap:6px;white-space:nowrap}
.brand-dot{width:20px;height:20px;border-radius:50%;background:var(--blue);flex:none}
.contact{position:absolute;top:0;height:67px;display:flex;align-items:center;gap:8px;color:var(--header-text);font-size:11.5px}
.contact svg{stroke:var(--header-text);fill:none;stroke-width:1.2}
.sep{position:absolute;left:400px;top:23px;width:1px;height:21px;background:#4a5055}
.user{position:absolute;right:35px;top:0;height:67px;display:flex;align-items:center;gap:8px;color:var(--header-text);font-size:12px}
.caret{width:0;height:0;border-left:5px solid transparent;border-right:5px solid transparent;border-top:6px solid var(--orange);margin-right:12px;margin-top:3px}
.avatar{width:22px;height:22px;border-radius:50%;background:#8e959c}
.sidebar{position:absolute;left:0;top:67px;width:194px;height:533px;background:var(--sidebar)}
.nav-item{position:absolute;left:0;width:194px;display:flex;align-items:center;color:var(--nav-text);font-size:11.5px;padding-left:30px;gap:14px;line-height:1.2}
.nav-item svg{flex:none;stroke:#9aa1a8;fill:none;stroke-width:1.2}
.nav-item.active{top:0;height:55px;background:var(--sidebar-active);color:var(--blue);border-left:5px solid var(--blue);padding-left:25px}
.nav-item.active svg{stroke:var(--blue)}
.nav-item.active::after{content:"";position:absolute;right:-1px;top:21px;border-top:7px solid transparent;border-bottom:7px solid transparent;border-right:7px solid #fff}
.page-title{position:absolute;left:194px;top:67px;width:870px;height:55px;display:flex;align-items:center;justify-content:flex-end;padding-right:35px;gap:20px;font-size:20px;color:var(--ink);font-weight:300}
.title-btn{width:23px;height:23px;background:var(--orange);display:flex;align-items:center;justify-content:center}
.title-btn i{border-left:5px solid transparent;border-right:5px solid transparent;border-top:6px solid #fff}
.band{position:absolute;left:194px;top:122px;width:870px;height:228px;background:var(--band)}
.card{position:absolute;top:140px;width:254px;height:182px;background:var(--card);text-align:center}
.badge{position:absolute;left:50%;top:-9px;margin-left:-9px;width:18px;height:18px;border-radius:50%;background:var(--header);color:#fff;font-size:10px;font-weight:700;line-height:18px}
.badge.alert{background:var(--green)}
.card h2{font-size:12.5px;font-weight:500;color:var(--ink);height:43px;padding-top:24px;line-height:14px;border-bottom:1px solid var(--line)}
.amount{font-size:27px;font-weight:700;color:var(--blue);margin-top:13px}
.meta{font-size:8.8px;color:var(--muted);line-height:13.6px;margin-top:10px}
.actions{position:absolute;left:0;right:0;top:143px;display:flex;justify-content:center;gap:3px}
.btn{background:var(--orange);color:#fff;font-size:9.5px;height:22px;line-height:22px;padding:0 24px;border-radius:2px}
.legend{position:absolute;top:332px;right:35px;display:flex;gap:24px;font-size:8.8px;color:#444}
.legend span{display:flex;align-items:center;gap:5px}
.dot{width:11px;height:11px;border-radius:50%;color:#fff;font-size:7.5px;font-weight:700;text-align:center;line-height:11px;font-style:normal}
.dot.g{background:var(--green)}.dot.b{background:var(--brown)}
.panel{position:absolute;top:362px;height:220px;border:1px solid var(--line);background:#fff}
.panel-head{height:31px;background:var(--panel-head);display:flex;align-items:center;gap:8px;padding-left:10px;font-size:13px;font-weight:500;color:var(--ink)}
.panel-head svg{stroke:var(--ink);fill:none;stroke-width:1.3}
table{border-collapse:collapse;table-layout:fixed;width:100%;font-size:8.8px;color:#333}
th{font-weight:400;color:var(--col-head);font-size:10px;text-align:left;padding-left:10px;height:32px;border-right:1px solid var(--line)}
td{height:31.5px;padding-left:10px;border-right:1px solid var(--line);border-top:1px solid var(--line);line-height:11px}
tr:nth-child(even) td{background:#f6f7f8}
th:last-child,td:last-child{border-right:none}
td.num{text-align:right;padding-right:10px;padding-left:0}
.q{display:inline-block;width:17px;height:17px;border-radius:50%;background:var(--brown);color:#fff;text-align:center;line-height:17px;font-size:10px;font-weight:700;margin-left:-2px}
</style>
</head>
<body>
<div class="app">
  <header class="topbar">
    <div class="brand"><span class="brand-dot"></span>Tradevane Credit</div>
    <div class="contact" style="left:228px">
      <svg width="14" height="14" viewBox="0 0 14 14"><circle cx="7" cy="7" r="6.3"/><path d="M4.5 4c0 3 2.5 5.5 5.5 5.5l.7-1.3-1.5-.8-.7.7c-.9-.4-1.7-1.2-2.1-2.1l.7-.7-.8-1.5z"/></svg>
      Support: 800-555-0142
    </div>
    <div class="sep"></div>
    <div class="contact" style="left:427px">
      <svg width="14" height="10" viewBox="0 0 14 10"><rect x=".6" y=".6" width="12.8" height="8.8"/><path d="M.6.6 7 5.5 13.4.6"/></svg>
      help@tradevanecredit.example
    </div>
    <div class="user"><span class="caret"></span><span class="avatar"></span>ac101@member.example</div>
  </header>

  <nav class="sidebar">
    <div class="nav-item active">
      <svg width="20" height="16" viewBox="0 0 20 16"><path d="M2.5 14a8 8 0 1 1 15 0z"/><path d="M10 10 13.5 5"/></svg>DASHBOARD</div>
    <div class="nav-item" style="top:71px;height:25px">
      <svg width="20" height="20" viewBox="0 0 20 20"><path d="M3 17 13 7M14 3l3 3-3 3-3-3zM3 3l4 4M17 17l-5-5"/></svg>JOB CENTER</div>
    <div class="nav-item" style="top:125px;height:25px">
      <svg width="20" height="14" viewBox="0 0 20 14"><rect x=".6" y=".6" width="18.8" height="12.8"/><path d="M.6 4h18.8M3 9h6"/></svg>PAYMENTS</div>
    <div class="nav-item" style="top:178px;height:30px">
      <svg width="20" height="18" viewBox="0 0 20 18"><path d="M1 6 10 1l9 5zM3 7v8M7 7v8M13 7v8M17 7v8M1 17h18"/></svg>CREDIT<br>MANAGEMENT</div>
    <div class="nav-item" style="top:236px;height:25px">
      <svg width="16" height="20" viewBox="0 0 16 20"><path d="M1 1h10l4 4v14H1z"/><path d="M4 8h8M4 11h8M4 14h8"/></svg>PRELIEN CENTER</div>
  </nav>

  <div class="page-title">Dashboard<span class="title-btn"><i></i></span></div>

  <section class="band"></section>

  <article class="card" style="left:230px">
    <span class="badge">i</span>
    <h2>AVAILABLE MASTER CREDIT</h2>
    <div class="amount">$129,500.00</div>
    <p class="meta" style="margin-top:16px">Master Credit Limit: $250,000.00</p>
    <div class="actions"><span class="btn">Setup New Job</span></div>
  </article>
  <article class="card" style="left:502px">
    <span class="badge">i</span>
    <h2>LAST PAYMENT</h2>
    <div class="amount">$500.00</div>
    <p class="meta" style="margin-top:16px">Last Payment Date: 6/28/2016</p>
    <div class="actions"><span class="btn">Veiw Payments</span><span class="btn" style="padding:0 25px">Veiw Billings</span></div>
  </article>
  <article class="card" style="left:775px">
    <span class="badge alert">!</span>
    <h2>NEXT PAYMENT</h2>
    <div class="amount">$158.95</div>
    <p class="meta">Due Date: 7/11/2016<br>Current Principal: $9,968.46<br>Minimum Interest/Fees: $158.95</p>
    <div class="actions"><span class="btn">Make Payment</span></div>
  </article>

  <div class="legend">
    <span><i class="dot g">!</i>Indicates an action is required</span>
    <span><i class="dot b">?</i>Information only - no action required</span>
  </div>

  <section class="panel" style="left:229px;width:392px">
    <div class="panel-head">
      <svg width="16" height="17" viewBox="0 0 16 17"><rect x="1" y="2.5" width="14" height="13.5"/><path d="M5 1h6v3H5zM4 8h8M4 11h8"/></svg>Task Summary</div>
    <table>
      <colgroup><col style="width:32px"><col style="width:134px"><col style="width:133px"><col></colgroup>
      <tr><th></th><th>Task</th><th>Status</th><th>Received</th></tr>
      <tr><td><span class="q">?</span></td><td>Supplier Invoice</td><td>Confirmation by Account Manager Pending</td><td>5/01/2016</td></tr>
      <tr><td></td><td></td><td></td><td></td></tr>
      <tr><td></td><td></td><td></td><td></td></tr>
      <tr><td></td><td></td><td></td><td></td></tr>
      <tr><td></td><td></td><td></td><td></td></tr>
    </table>
  </section>

  <section class="panel" style="left:637px;width:392px">
    <div class="panel-head">
      <svg width="16" height="17" viewBox="0 0 16 17"><rect x="1" y="2.5" width="14" height="13.5"/><path d="M5 1h6v3H5zM4.5 10l2.5 2.5 4.5-5"/></svg>Active Jobs</div>
    <table>
      <colgroup><col style="width:77px"><col style="width:84px"><col style="width:67px"><col style="width:90px"><col></colgroup>
      <tr><th>Job#</th><th>Job Name</th><th>Status</th><th style="padding-left:13px">Credit Limit</th><th>Avail. Credit</th></tr>
      <tr><td>pc101-001</td><td>Job-001</td><td>Active</td><td class="num">$50,100.00</td><td class="num">$35,100.00</td></tr>
      <tr><td>pc101-002</td><td>Job-002</td><td>Active</td><td class="num">$40,000.00</td><td class="num">$2000.00</td></tr>
      <tr><td>pc101-003</td><td>Job-003</td><td>Active</td><td class="num">$22,000.00</td><td class="num">$0.00</td></tr>
      <tr><td>pc101-004</td><td>Job-004</td><td>Active</td><td class="num">$10,400.00</td><td class="num">$10,400.00</td></tr>
      <tr><td></td><td></td><td></td><td></td><td></td></tr>
    </table>
  </section>
</div>
</body>
</html>
```